QWTORAMX ( Wordpress website for catalogue of Zintrop Cast Pages)

Need a website to showcase different Zintrop Cast pages ( in different categories). Similar to e-commerce except no check-out / purchase of items. Pls use our logos provided and color scheme to be white+red+ blue as per our logo.

Target Market(s)

Consumers

Font styles to use
Sans Serif

Colors
ffffff
ec1f27
3276b5

Requirements
Must have
• I will need a Wordpress Theme as a handover. Also, pls use the color scheme (red+blue+white) as per logo attached. Prefer clean and near design with white space.

```html
<!DOCTYPE html>
<html lang="en">
<head>
<meta charset="utf-8">
<title>QWTORAMX – Categories Listing</title>
<link href="https://fonts.googleapis.com/css2?family=Figtree:wght@400;500;700;800&display=swap" rel="stylesheet">
<style>
:root{
  --white:#ffffff;
  --red:#ec1f27;
  --blue:#3276b5;
  --ink:#0d1826;
  --text:#222a33;
  --muted:#5a6069;
  --banner:#f7f7f8;
  --footer:#f4f4f5;
  --rule:#d9dadd;
  --label:rgba(40,40,40,.78);
}
*{margin:0;padding:0;box-sizing:border-box}
html,body{width:1188px;height:1200px;overflow:hidden;background:var(--white)}
body{position:relative;font-family:"Figtree",Arial,sans-serif;color:var(--text)}
.abs{position:absolute}
.brand{font-weight:800;font-size:23px;letter-spacing:.5px;color:var(--blue);line-height:1}
.site-header .brand{left:232px;top:19px}
.main-nav{left:539px;top:24px;font-size:10.5px;font-weight:500;letter-spacing:.2px}
.main-nav a{color:var(--text);text-decoration:none;position:absolute;white-space:nowrap}
.hero{left:0;top:60px;width:1188px;height:167px;background:var(--banner);overflow:hidden}
.hero-deco-left{left:0;top:0;width:380px;height:167px;background:radial-gradient(ellipse at 10% 30%,rgba(236,31,39,.16),transparent 60%),radial-gradient(ellipse at 30% 60%,rgba(50,118,181,.16),transparent 60%)}
.hero-deco-right{right:0;top:0;width:270px;height:167px;background:linear-gradient(120deg,transparent 20%,rgba(245,180,120,.35) 40%,rgba(120,200,220,.4) 60%,rgba(240,150,180,.3) 80%,rgba(120,200,220,.35))}
.hero h1{position:absolute;left:0;right:0;top:66px;text-align:center;font-size:30px;font-weight:800;color:var(--ink);letter-spacing:.2px}
.category{width:167px;height:167px;border-radius:6px;overflow:hidden}
.category .photo{position:absolute;inset:0}
.category .tag{position:absolute;left:6px;right:6px;bottom:6px;height:30px;border-radius:5px;background:var(--label);color:var(--white);font-weight:800;font-size:12.5px;display:flex;align-items:center;justify-content:center;letter-spacing:.2px}
.category .tag.clear{background:transparent}
.site-footer{left:0;top:895px;width:1188px;height:305px;background:var(--footer)}
.wave{left:0;top:880px}
.site-footer .brand{left:232px;top:60px}
.contact{display:flex;gap:12px;align-items:flex-start;white-space:nowrap}
.contact h4{font-size:12.5px;font-weight:700;color:var(--ink);letter-spacing:.2px}
.contact p{font-size:10.5px;color:var(--muted);margin-top:6px}
.divider{width:1px;height:37px;background:var(--rule);top:52px}
.social{width:31px;height:31px;border-radius:50%;background:var(--white);border:1px solid #e4e5e7;top:132px}
.social.primary{border-color:var(--red)}
.footer-nav{left:0;width:1188px;top:202px;display:flex;justify-content:center;gap:20px;font-size:10.5px;font-weight:500}
.footer-nav a{color:var(--text);text-decoration:none}
.footer-nav span{color:var(--text)}
.footer-rule{left:232px;top:258px;width:724px;height:1px;background:var(--rule)}
.copyright{left:0;width:1188px;top:276px;text-align:center;font-size:9.5px;color:var(--muted)}
</style>
</head>
<body>

<header class="site-header">
  <div class="brand abs">QWTORAMX</div>
  <nav class="main-nav abs">
    <a style="left:0">HOME</a>
    <a style="left:64px">ABOUT</a>
    <a style="left:132px">CATEGORIES</a>
    <a style="left:230px">FAQS</a>
    <a style="left:289px">BLOG</a>
    <a style="left:349px">CONTACT US</a>
  </nav>
</header>

<section class="hero abs">
  <div class="hero-deco-left abs" role="img" aria-label="Scattered red and blue stars"></div>
  <div class="hero-deco-right abs" role="img" aria-label="Colourful diagonal paint strokes"></div>
  <h1>CATEGORIES LISTING</h1>
</section>

<main>
  <a class="category abs" style="left:232px;top:301px"><div class="photo" role="img" aria-label="Pizzas on a dark table" style="background:linear-gradient(160deg,#3a2a1e,#b0652f 45%,#1c1a18)"></div><span class="tag clear">FOOD</span></a>
  <a class="category abs" style="left:417.5px;top:301px"><div class="photo" role="img" aria-label="Coats hanging on a rail" style="background:linear-gradient(120deg,#8c6a48,#c9a680 45%,#e8e2d8)"></div><span class="tag">CLOTHING</span></a>
  <a class="category abs" style="left:603px;top:301px"><div class="photo" role="img" aria-label="Legs in heels and a dotted dress" style="background:linear-gradient(120deg,#9e8e80,#d9c8bc 55%,#b0a39a)"></div><span class="tag">FASHION</span></a>
  <a class="category abs" style="left:789px;top:301px"><div class="photo" role="img" aria-label="Traveller with arms raised on a beach" style="background:linear-gradient(180deg,#cfd6de,#b9a79a 55%,#e0a56a 75%,#7a6a5e)"></div><span class="tag">TRAVEL</span></a>

  <a class="category abs" style="left:232px;top:487px"><div class="photo" role="img" aria-label="Restaurant interior with pendant lamps" style="background:linear-gradient(170deg,#6f6a5e,#b49054 55%,#4a3626)"></div><span class="tag clear">RESTAURANT</span></a>
  <a class="category abs" style="left:417.5px;top:487px"><div class="photo" role="img" aria-label="Runner tying an orange shoe" style="background:linear-gradient(150deg,#d9b39a,#8c5a4a 50%,#d2552a 75%,#6d4a3e)"></div><span class="tag">SPORTS</span></a>
  <a class="category abs" style="left:603px;top:487px"><div class="photo" role="img" aria-label="Small dog running on grass" style="background:linear-gradient(160deg,#6b7f3e,#a99a7a 50%,#4e6a2a)"></div><span class="tag">PET SERVICES</span></a>
  <a class="category abs" style="left:789px;top:487px"><div class="photo" role="img" aria-label="Doctor holding a family symbol" style="background:linear-gradient(140deg,#9fd1ea,#e6eef3 55%,#8fc6e4)"></div><span class="tag">HEALTH</span></a>

  <a class="category abs" style="left:232px;top:673px"><div class="photo" role="img" aria-label="Dental check-up scene" style="background:linear-gradient(150deg,#b9a69a,#e2cfc4 55%,#cdbdb4)"></div><span class="tag">DENTIST</span></a>
  <a class="category abs" style="left:417.5px;top:673px"><div class="photo" role="img" aria-label="Hand writing with a pen" style="background:linear-gradient(140deg,#d8b3a4,#eadfdb 55%,#9fb4c9)"></div><span class="tag">EDUCATION</span></a>
  <a class="category abs" style="left:603px;top:673px"><div class="photo" role="img" aria-label="Children playing in a park" style="background:linear-gradient(170deg,#8ba35a,#c9c2b0 50%,#5f7a3a)"></div><span class="tag">ENTERTAINMENT</span></a>
  <a class="category abs" style="left:789px;top:673px"><div class="photo" role="img" aria-label="Calculator and paperwork on a desk" style="background:linear-gradient(150deg,#d7c2a6,#e8e6e2 50%,#b89a7e)"></div><span class="tag">ACCOUNTING</span></a>
</main>

<svg class="wave abs" width="1188" height="40" viewBox="0 0 1188 40"><path d="M0 40 C300 5 500 5 700 22 S1000 40 1188 20 V40 Z" fill="var(--footer)"/></svg>

<footer class="site-footer abs">
  <div class="brand abs">QWTORAMX</div>

  <div class="contact abs" style="left:417px;top:56px">
    <svg width="26" height="26" viewBox="0 0 26 26" fill="none" stroke="var(--ink)" stroke-width="1.3"><path d="M5 3l4 4-2 3c1.5 3 4 5.5 7 7l3-2 4 4-3 3C10 22 4 16 2 6z"/><path d="M15 4a7 7 0 0 1 7 7M15 8a3 3 0 0 1 3 3" stroke="var(--red)"/></svg>
    <div><h4>CALL US</h4><p>321 7654 0098</p></div>
  </div>
  <div class="divider abs" style="left:565px"></div>

  <div class="contact abs" style="left:602px;top:56px">
    <svg width="25" height="26" viewBox="0 0 25 26" fill="none" stroke="var(--ink)" stroke-width="1.3"><path d="M2 10l10.5-8L23 10v14H2z"/><path d="M2 10l10.5 8L23 10M2 24l8-7M23 24l-8-7"/><circle cx="12.5" cy="9" r="3" stroke="var(--red)"/></svg>
    <div><h4>EMAIL</h4><p>hi@qwtoramx.net</p></div>
  </div>
  <div class="divider abs" style="left:752px"></div>

  <div class="contact abs" style="left:789px;top:56px">
    <svg width="20" height="26" viewBox="0 0 20 26" fill="none" stroke="var(--ink)" stroke-width="1.3"><path d="M10 25S2 15 2 10a8 8 0 0 1 16 0c0 5-8 15-8 15z"/><circle cx="10" cy="10" r="3" stroke="var(--red)"/></svg>
    <div><h4>ADDRESS</h4><p>Lorem ipsum dolor sit amet.</p></div>
  </div>

  <a class="social primary abs" style="left:520px" aria-label="Zintrop"></a>
  <a class="social abs" style="left:578px" aria-label="Picvault"></a>
  <a class="social abs" style="left:637px" aria-label="Chirpline"></a>

  <nav class="footer-nav abs">
    <a>HOME</a><span>I</span><a>ABOUT</a><span>I</span><a>CATEGORIES</a><span>I</span><a>FAQS</a><span>I</span><a>BLOG</a><span>I</span><a>CONTACT US</a>
  </nav>
  <div class="footer-rule abs"></div>
  <p class="copyright abs">Copyright © 2020 QWTORAMX. All rights reserved.</p>
</footer>

</body>
</html>
```